TK Drafting

Simple Design - Logo is done (from this site). Logo on one side - Back Side an image or outline of a house blue print - My name, phone, email, website url. Prefer the traditional Architectural style of letters -

Target Market(s)

Customers who need a floor plan redesigned for renovations or realtors who want a floor plan for marketing their listings

Industry/Entity Type

Architecture

Contact Information for Business Card

Colby Faust - Name
415-362-8840 - Phone
tkdraftingco@mailpost.example
www.tkdraftingco.example

Font styles to use
Other font styles liked:
• Architecture writing -

Colors
0555a3
3276b5
85acd3

Requirements
Must have
• Logo that is attached. I like an indigo blue color for the background or a royal blue - gray logo OR - white and clean with the logo on one side and the same color gray lettering on the other side
Nice to have
• some sort of image that shows a residential blue print. It may not be possible on this small of a card though.
Should not have
• Nothing cartoonish.

```html
<!DOCTYPE html>
<html lang="en">
<head>
<meta charset="utf-8">
<title>TK Drafting — Business Card</title>
<link href="https://fonts.googleapis.com/css2?family=Arimo:wght@400;700&display=swap" rel="stylesheet">
<style>
  :root {
    --backdrop: #1b1c1e;
    --card-blue: #85acd3;
    --edge-blue: #0555a3;
    --mid-blue: #3276b5;
    --ink-white: #ffffff;
    --emboss-blue: #5e8fc2;
  }
  * { margin: 0; padding: 0; box-sizing: border-box; }
  html, body {
    width: 1200px;
    height: 820px;
    overflow: hidden;
    background: var(--backdrop);
    font-family: "Arimo", Arial, sans-serif;
  }
  .sheet {
    width: 1200px;
    height: 820px;
    display: flex;
    flex-direction: column;
    align-items: center;
    justify-content: center;
    gap: 28px;
  }
  .card {
    position: relative;
    width: 640px;
    height: 366px;
    background: var(--card-blue);
    border-bottom: 3px solid var(--edge-blue);
    border-left: 2px solid var(--edge-blue);
  }

  /* Front: contact side */
  .brand {
    position: absolute;
    right: 92px;
    top: 118px;
    display: flex;
    align-items: center;
    gap: 12px;
    color: var(--ink-white);
    font-weight: 400;
    font-size: 38px;
    letter-spacing: 3px;
    text-transform: uppercase;
  }
  .brand-mark {
    width: 16px;
    height: 16px;
    background: var(--ink-white);
  }
  .rule {
    position: absolute;
    left: 92px;
    right: 50px;
    top: 262px;
    height: 1.5px;
    background: var(--ink-white);
  }
  .holder-name {
    position: absolute;
    left: 92px;
    top: 234px;
    color: var(--ink-white);
    font-weight: 700;
    font-size: 19px;
    letter-spacing: 0.5px;
    text-transform: uppercase;
  }
  .contact-list {
    position: absolute;
    left: 92px;
    top: 274px;
    list-style: none;
    color: var(--ink-white);
    font-size: 14px;
    line-height: 22px;
  }
  .contact-list li {
    display: flex;
    align-items: center;
    gap: 8px;
  }
  .contact-list svg {
    width: 13px;
    height: 13px;
    flex: none;
  }

  /* Back: brand side */
  .brand-back {
    position: absolute;
    left: 50%;
    top: 50%;
    transform: translate(-50%, -50%);
    display: flex;
    align-items: center;
    gap: 12px;
    color: var(--emboss-blue);
    font-weight: 400;
    font-size: 36px;
    letter-spacing: 3px;
    text-transform: uppercase;
  }
  .brand-back .brand-mark { background: var(--emboss-blue); }
</style>
</head>
<body>
<main class="sheet">
  <section class="card card-front" aria-label="Business card front">
    <div class="brand"><span class="brand-mark"></span>TK Drafting</div>
    <p class="holder-name">Colby Faust</p>
    <div class="rule"></div>
    <ul class="contact-list">
      <li>
        <svg viewBox="0 0 16 16" aria-hidden="true"><path fill="#fff" d="M3.6 1.2l2.3 2.6-1.3 1.7c.9 2 2.4 3.6 4.4 4.6l1.7-1.3 2.6 2.3-1.4 2.6C6.9 13.6 2.3 9 1 3.6z"/></svg>
        415-362-8840
      </li>
      <li>
        <svg viewBox="0 0 16 16" aria-hidden="true"><rect x="1" y="3" width="14" height="10" fill="#fff"/><path d="M1 3l7 6 7-6" fill="none" stroke="#85acd3" stroke-width="1.4"/></svg>
        tkdraftingco@mailpost.example
      </li>
      <li>
        <svg viewBox="0 0 16 16" aria-hidden="true"><g fill="none" stroke="#fff" stroke-width="1.3"><circle cx="8" cy="8" r="6.5"/><ellipse cx="8" cy="8" rx="3" ry="6.5"/><path d="M1.5 8h13M2.6 4.6h10.8M2.6 11.4h10.8"/></g></svg>
        www.tkdraftingco.example
      </li>
    </ul>
  </section>

  <section class="card card-back" aria-label="Business card back">
    <div class="brand-back"><span class="brand-mark"></span>TK Drafting</div>
  </section>
</main>
</body>
</html>
```